ALL I NEED IS A BUSINESS CARD AND LETTER HEAD OFFICIAL PAPER

i only need a letter head ( sample attached)
along with business cards.
i will upload a sample ,along with the logo of both companies that should be on the letter head and business cards.

Note:its a high end maritime solution company

Company name is Haldwick Norcrest Africa

slogan : For maritime solution ( it could be on the back side of the business card)
Updates

Project Deadline Extended Reason: Hi Guys, thanks for your designs , i am sorry but now we just changed the company name toLuerssen Norcrest Africa slogan For Maritime solutions. i hope you can help me with that! slogan could be in the back side or any place, but not next to the title . and both logos of norcrest and haldwik should be there. thank you Added Sunday, March 1, 2015

Industry/Entity Type

Business

Contact Information for Business Card

as attached, please provide more designs

Font styles to use
Serif

Requirements
Must have
• SAME AS THE BUSINESS LETTER,
• Haldwick Norcrest Africa
• slogan for Maritime Solutions

```html
<!DOCTYPE html>
<html lang="en">
<head>
<meta charset="utf-8">
<title>Haldwick Norcrest African Maritime Solutions – Letterhead</title>
<link rel="stylesheet" href="https://fonts.googleapis.com/css2?family=Michroma&family=Open+Sans:wght@400;700&display=swap">
<style>
  :root {
    --navy: #2b2d82;
    --navy-deep: #1c1d5e;
    --blue-light: #8c8fd6;
    --blue-pale: #c9cbee;
    --ink: #0b0b0f;
    --paper: #ffffff;
    --stage: #e6e6e8;
    --logo-grey: #d8d8dc;
  }
  * { box-sizing: border-box; margin: 0; padding: 0; }
  html, body {
    width: 900px; height: 1200px; overflow: hidden;
    background: var(--stage);
  }
  .letterhead {
    position: absolute; left: 60px; top: 48px;
    width: 773px; height: 1093px;
    background: var(--paper);
    box-shadow: 0 2px 10px rgba(0,0,0,.25);
  }
  .letterhead__header { position: absolute; left: 0; top: 0; width: 773px; height: 112px; display: block; }
  .company-name {
    font-family: "Michroma", sans-serif;
    font-size: 14px; fill: #fff;
  }
  .partner-name { font-family: "Open Sans", sans-serif; font-weight: 700; font-size: 17px; letter-spacing: 1px; }
  .partner-name--light { fill: var(--logo-grey); }
  .partner-name--navy { fill: var(--navy); }
  .contact-text { font-family: "Open Sans", sans-serif; font-size: 14px; fill: #fff; }
  .letterhead__footer {
    position: absolute; left: 0; top: 1058px; width: 773px; height: 24px;
    background: linear-gradient(90deg, var(--blue-pale) 0%, var(--navy) 30%, var(--navy) 70%, var(--blue-pale) 100%);
    color: #fff; font-family: "Open Sans", sans-serif; font-size: 15px;
    text-align: center; line-height: 24px;
  }
</style>
</head>
<body>
<main class="letterhead">
  <svg class="letterhead__header" viewBox="0 0 773 112" xmlns="http://www.w3.org/2000/svg" aria-label="Letterhead header">
    <defs>
      <linearGradient id="bandLeft" x1="0" x2="1" y1="0" y2="0">
        <stop offset="0" stop-color="#7679cc"/>
        <stop offset="0.35" stop-color="#3a3c94"/>
        <stop offset="0.8" stop-color="#1e1f63"/>
        <stop offset="1" stop-color="#111233"/>
      </linearGradient>
      <linearGradient id="bandRight" x1="0" x2="1" y1="0" y2="0">
        <stop offset="0" stop-color="#1c1d5e"/>
        <stop offset="0.6" stop-color="#2b2d82"/>
        <stop offset="1" stop-color="#b3b5e6"/>
      </linearGradient>
      <linearGradient id="contactBar" x1="0" x2="1" y1="0" y2="0">
        <stop offset="0" stop-color="#8a8a8a"/>
        <stop offset="0.06" stop-color="#0b0b0f"/>
        <stop offset="0.88" stop-color="#0b0b0f"/>
        <stop offset="1" stop-color="#8f8f8f"/>
      </linearGradient>
    </defs>

    <rect class="top-rule" x="0" y="20" width="773" height="4" fill="var(--navy)"/>

    <polygon class="band-left" points="0,30 372,30 358,82 0,82" fill="url(#bandLeft)"/>
    <text class="company-name" x="42" y="51" textLength="314" lengthAdjust="spacingAndGlyphs">HALDWICK NORCREST AFRICAN</text>
    <text class="company-name" x="86" y="74" textLength="226" lengthAdjust="spacingAndGlyphs">MARITIME SOLUTIONS</text>

    <polygon class="band-partner-dark" points="380,30 520,30 505,82 366,82" fill="var(--ink)"/>
    <text class="partner-name partner-name--light" x="443" y="63" text-anchor="middle">HALDWICK</text>

    <text class="partner-name partner-name--navy" x="574" y="63" text-anchor="middle">NORCREST</text>

    <polygon class="band-right" points="648,30 773,30 773,82 634,82" fill="url(#bandRight)"/>

    <rect class="contact-bar" x="0" y="86" width="773" height="24" fill="url(#contactBar)"/>

    <g class="contact contact--phone">
      <rect x="37" y="90" width="15" height="15" rx="2" fill="var(--navy)"/>
      <path d="M41.5 93 l2 0 l.8 2.6 l-1.3 1 q1 2.2 3 3 l1 -1.3 l2.6 .8 l0 2 q-7 .3 -8.1 -8.1 z" fill="#fff"/>
      <text class="contact-text" x="61" y="103">: +971 2 555 0140</text>
    </g>
    <g class="contact contact--mobile">
      <rect x="306" y="90" width="15" height="15" rx="2" fill="var(--navy)"/>
      <rect x="310" y="92.5" width="7" height="10" rx="1" fill="#fff"/>
      <rect x="311.3" y="94" width="4.4" height="3.6" fill="var(--navy)"/>
      <text class="contact-text" x="330" y="103">: +971 2 555 0141</text>
    </g>
    <g class="contact contact--email">
      <rect x="566" y="90" width="17" height="15" rx="2" fill="var(--navy)"/>
      <rect x="569" y="93.5" width="11" height="8" fill="#fff"/>
      <path d="M569 93.5 l5.5 4.5 l5.5 -4.5 M569 101.5 l4 -3.5 M580 101.5 l-4 -3.5" stroke="var(--navy)" stroke-width="1" fill="none"/>
      <text class="contact-text" x="591" y="103" textLength="144" lengthAdjust="spacingAndGlyphs">: norcrest1@norcrest1.ae</text>
    </g>
  </svg>

  <footer class="letterhead__footer">P.O.Box : 204817 Abu Dhabi - UAE</footer>
</main>
</body>
</html>
```